QRV Supplements needs a label designer for supplement company

Looking for an on going label designer for my supplement company. I have three products that will need designs. I'm about to launch my sleep supplement called Velora Rest and that's the first design needed.
I would like all designs to be somewhat simple, not overstated and uniformed so that when you look at all of the labels of the different supplements they are similar and you can tell it's the same brand.
Please see attached sample pictures below as ideas.
Updates

The brand is QRV supplements, logo file has been provided. The supplement is called Velora Rest. It is a liquid supplement that is a 32/33 ounce white bottle. Die lines and measurements will be provided. Here's text for wording ideas: Wording: Natural Sleep Aid Reset your circadian rhythm. May help you: Fall asleep faster. Get a deeper more restful sleep. Boost Immune System Remember your dreams. Protect your brain and flush toxins. Wake up feeling refreshed. Non-gmo Gluten Free Sugar Free Vegan Manufactured in cGMP factory Manufactured in USA

Target Market(s)

Health and wellness/supplement industry for regular people not hardcore gym goers. My supplements are for a health lifestyle not bodybuilding.

Industry/Entity Type

Health And Wellness

Colors
3176b5
3276b5
33a6d7
85cae6
85abd2
cedeed
e4daeb
b7a5cd

Requirements
Must have
• There will be some text and wording that I will provide that must be on the bottles.

```html
<!DOCTYPE html>
<html lang="en">
<head>
<meta charset="utf-8">
<title>QRV Supplements — Velora Rest Label</title>
<link href="https://fonts.googleapis.com/css2?family=Montserrat:wght@200;300;400;600;700&family=Barlow+Condensed:wght@500;700&display=swap" rel="stylesheet">
<style>
  :root {
    --stage: #808080;
    --lavender: #b7a5cd;
    --lavender-soft: #c6b8da;
    --white: #ffffff;
    --ink: #1b1b2e;
  }
  * { box-sizing: border-box; margin: 0; padding: 0; }
  html, body { width: 1200px; height: 887px; overflow: hidden; }
  body {
    background: var(--stage);
    font-family: "Montserrat", sans-serif;
    position: relative;
  }
  .label {
    position: absolute;
    left: 139px; top: 85px;
    width: 917px; height: 710px;
    background: var(--lavender);
    box-shadow: 0 22px 18px -12px rgba(0,0,0,0.55);
    overflow: hidden;
  }
  .panel { position: absolute; top: 0; height: 710px; overflow: hidden; }
  .panel--front { left: 0; width: 417px; }
  .panel--back { left: 498px; width: 419px; }
  .panel__cap { position: absolute; left: 0; top: 0; width: 100%; height: 165px; }
  .brand {
    position: absolute; top: 58px; left: 0; width: 100%;
    display: flex; align-items: center; justify-content: center; gap: 12px;
  }
  .brand__dot {
    width: 56px; height: 56px; border-radius: 50%;
    border: 3px solid var(--ink);
  }
  .brand__name {
    font-family: "Barlow Condensed", sans-serif;
    font-weight: 700; font-size: 33px; letter-spacing: 0.3px;
    color: var(--ink); text-transform: uppercase;
  }
  .title { position: absolute; left: 0; width: 100%; text-align: center; color: var(--white); }
  .title__lead { top: 185px; font-weight: 200; font-size: 54px; letter-spacing: 2px; line-height: 1; }
  .title__main { top: 232px; font-weight: 700; font-size: 76px; letter-spacing: 1px; line-height: 1; }
  .title__sub { top: 303px; font-weight: 300; font-size: 24px; letter-spacing: -0.3px; line-height: 1; }
  .art {
    position: absolute; top: 345px; width: 214px; height: 214px;
    border-radius: 50%;
    background: radial-gradient(circle, var(--lavender-soft) 0%, rgba(255,255,255,0.55) 60%, rgba(183,165,205,0) 72%);
  }
  .panel--front .art { left: 119px; }
  .panel--back .art { left: 114px; }
  .tagline {
    position: absolute; top: 563px; left: 0; width: 100%;
    text-align: center; color: var(--white);
    font-weight: 300; font-size: 18px; line-height: 23px;
  }
  .tagline strong { font-weight: 700; }
  .net-weight {
    position: absolute; top: 635px; left: 0; width: 100%;
    text-align: center; color: var(--white);
    font-family: "Barlow Condensed", sans-serif; font-weight: 500; font-size: 14px;
  }
  .spine {
    position: absolute; left: 417px; top: 0; width: 81px; height: 710px;
    border-left: 2px solid var(--white); border-right: 2px solid var(--white);
  }
  .claims { list-style: none; }
  .claim {
    position: absolute; left: 0; width: 77px;
    display: flex; flex-direction: column; align-items: center; gap: 4px;
  }
  .claim__mark {
    width: 44px; height: 44px; border-radius: 50%;
    border: 2.5px solid var(--white);
  }
  .claim__text {
    color: var(--white); font-weight: 700; font-size: 7.5px;
    letter-spacing: 0.3px; line-height: 1.15; text-align: center; text-transform: uppercase;
  }
  .spine__note {
    position: absolute; top: 623px; left: 0; width: 100%;
    text-align: center; color: var(--white);
    font-size: 9.5px; line-height: 11.4px; font-weight: 400;
  }
</style>
</head>
<body>
  <main class="label">
    <section class="panel panel--front">
      <svg class="panel__cap" viewBox="0 0 417 165" preserveAspectRatio="none">
        <path d="M0 0 H417 V111 Q300 170 208 160 Q100 155 0 102 Z" fill="#ffffff"/>
      </svg>
      <div class="brand"><span class="brand__dot"></span><span class="brand__name">QRV Supplements</span></div>
      <p class="title title__lead">VELORA</p>
      <p class="title title__main">REST</p>
      <p class="title title__sub">NATURAL SLEEP AID</p>
      <div class="art" role="img" aria-label="Line illustration of a sleeping brain with moon, cloud and Z letters inside a dotted halo"></div>
      <p class="tagline">Fall Asleep <strong>Faster</strong><br>Stay Asleep <strong>Longer</strong></p>
      <p class="net-weight">Net Wt. 2 LBs (32oz)</p>
    </section>

    <section class="spine">
      <ul class="claims">
        <li class="claim" style="top:28px"><span class="claim__mark"></span><span class="claim__text">Vegan &amp;<br>Vegetarian</span></li>
        <li class="claim" style="top:113px"><span class="claim__mark"></span><span class="claim__text">Non-GMO</span></li>
        <li class="claim" style="top:194px"><span class="claim__mark"></span><span class="claim__text">Made in USA</span></li>
        <li class="claim" style="top:277px"><span class="claim__mark"></span><span class="claim__text">Sugar Free</span></li>
        <li class="claim" style="top:363px"><span class="claim__mark"></span><span class="claim__text">Gluten Free</span></li>
        <li class="claim" style="top:448px"><span class="claim__mark"></span><span class="claim__text">Lab Tested</span></li>
        <li class="claim" style="top:530px"><span class="claim__mark"></span><span class="claim__text">cGMP</span></li>
      </ul>
      <p class="spine__note">Manufactured<br>in<br>cGMP factory<br>Manufactured<br>in USA</p>
    </section>

    <section class="panel panel--back">
      <svg class="panel__cap" viewBox="0 0 419 165" preserveAspectRatio="none">
        <path d="M0 0 H419 V102 Q320 155 210 160 Q120 170 0 111 Z" fill="#ffffff"/>
      </svg>
      <div class="brand"><span class="brand__dot"></span><span class="brand__name">QRV Supplements</span></div>
      <p class="title title__lead">VELORA</p>
      <p class="title title__main">REST</p>
      <p class="title title__sub">NATURAL SLEEP AID</p>
      <div class="art" role="img" aria-label="Line illustration of a sleeping brain with moon, cloud and Z letters inside a dotted halo"></div>
      <p class="tagline">Fall Asleep <strong>Faster</strong><br>Stay Asleep <strong>Longer</strong></p>
      <p class="net-weight">Net Wt. 2 LBs (32oz)</p>
    </section>
  </main>
</body>
</html>
```